Leadvista.com ;Take Yourself Up to the Next Level. More success, higher productivity, better health.

PLEASE READ IT CAREFULLY
I HAVE RECEIVED SOME FIRST DESIGNS AND I HAVE A FEELING THAT ALMOST NOBODY HAS READ THE BRIEFING CAREFULLY.

What I need actually is the design of the main visual
THE MAIN VISUAL MUST COMMUNICATE THE CONCEPT.
THIS WEBSITE IS ABOUT THE PERSONAL DEVELOPMENT.

The change of the main visual may be linked with other changes of other elements of the homepage, but this is the secondary task.

BACKGROUND
I have launched a blog on healthy productivity: leadvista.com

The problem is that the main visual does not communicate clearly what the website is about.

Currently I have a blog with advice on healthy productivity and a shop. In teh future I would like to offer stress management courses, fitness boot camps for executives, mindefulness courses, courses for healthy sleep and work-life balance.

The task is to develop the homepage which communicates the current positioning:

Lead Vista-
Take Yourself Up to the Next Level. More Success, Higher Productivity, Better Health.

The homepage should contain all the blocks of the current homepage. Actually the main task is to find the powerful design representation of the website positioning.
Updates

Low design quality

Target Market(s)

US executives, managers and entrepreneurs

Requirements
Must have
• You should keep in principle the current color code which is green, blue, grey
• The design project must contain all the current homepage elements like blog, testimonial, footnote etc

```html
<!DOCTYPE html>
<html lang="en">
<head>
<meta charset="utf-8">
<title>Leadvista.com – Take Yourself Up to the Next Level</title>
<link href="https://fonts.googleapis.com/css2?family=Montserrat:wght@500;600;700&family=Open+Sans:wght@400;600;700;800&display=swap" rel="stylesheet">
<style>
:root{
  --green:#6cbb2c;
  --blue:#16a6e3;
  --blue-dark:#1677c8;
  --grey-bg:#f3f0f0;
  --panel:#555555;
  --ink:#1d1d1d;
  --text:#444444;
  --footer:#222222;
  --white:#ffffff;
}
*{margin:0;padding:0;box-sizing:border-box}
html,body{width:1200px;height:4307px;overflow:hidden}
body{position:relative;font-family:'Open Sans',sans-serif;color:var(--text);background:var(--white)}
.abs{position:absolute}
.btn{position:absolute;background:var(--green);color:var(--white);font-family:'Montserrat',sans-serif;font-weight:700;display:flex;align-items:center;justify-content:center;letter-spacing:.3px}

/* header */
.site-header{position:absolute;left:0;top:0;width:1200px;height:113px;background:var(--white)}
.brand{position:absolute;display:flex;align-items:center;gap:14px}
.brand-name{font-family:'Open Sans',sans-serif;font-weight:400;letter-spacing:4px}
.brand-dot{width:30px;height:30px;border-radius:50%;background:var(--green)}
.follow{position:absolute;left:636px;top:32px;display:flex;align-items:center;gap:6px;font-size:10px;font-weight:700;color:var(--ink)}
.follow span.s{width:19px;height:19px;border-radius:50%;background:var(--blue-dark)}
.follow span.s.r{background:#d0342c}
.follow span.s.g{background:#333}
.nav{position:absolute;left:459px;top:80px;display:flex;gap:33px;font-family:'Montserrat',sans-serif;font-size:12px;font-weight:600;color:var(--ink)}
.nav .on{color:var(--green)}

/* hero */
.hero{position:absolute;left:0;top:113px;width:1200px;height:541px;background:linear-gradient(170deg,#f2b64e 0%,#d78a2c 35%,#8a5a1e 70%,#4a3512 100%)}
.hero-text{position:absolute;left:669px;top:92px;color:var(--white)}
.hero-text h1{font-family:'Montserrat',sans-serif;font-weight:600;font-size:40px;line-height:1}
.hero-text p{font-size:26px;margin-top:16px}
.hero-text ul{list-style:none;margin-top:20px}
.hero-text li{font-weight:800;font-size:27px;line-height:44px;display:flex;align-items:center;gap:16px}
.dots{position:absolute;left:573px;top:489px;display:flex;gap:6px}
.dots i{width:7px;height:7px;border-radius:50%;background:#fff}
.dots i.on{background:var(--green)}

/* topics */
.topics{position:absolute;left:0;top:654px;width:1200px;height:653px;background:var(--grey-bg)}
.sec-title{position:absolute;left:0;width:1200px;text-align:center;font-family:'Montserrat',sans-serif;font-weight:600;color:var(--ink)}
.card{position:absolute;width:223px;height:210px;background:var(--white);display:flex;flex-direction:column;align-items:center;justify-content:flex-start;padding-top:38px;text-align:center;font-family:'Montserrat',sans-serif;font-size:13px;font-weight:600;color:var(--ink);line-height:20px}
.card svg{margin-bottom:18px}
.card.active{background:var(--blue);color:var(--white)}
.card.active .rm{margin-top:10px;border:1px solid #fff;font-size:9px;padding:2px 8px;line-height:16px}
.card.all{background:var(--green);color:var(--white);justify-content:center;padding-top:0;font-size:15px;font-weight:700}

/* welcome */
.welcome-img{position:absolute;left:0;top:1307px;width:663px;height:493px;background:linear-gradient(180deg,#e9eef2 0%,#9aa6b2 40%,#3a4452 80%,#232a34 100%)}
.welcome{position:absolute;left:663px;top:1307px;width:537px;height:493px;background:var(--panel);color:var(--white)}
.welcome h3{position:absolute;left:70px;top:66px;font-family:'Montserrat',sans-serif;font-weight:600;font-size:28px}
.welcome h2{position:absolute;left:70px;top:100px;font-family:'Montserrat',sans-serif;font-weight:700;font-size:38px}
.welcome p{position:absolute;left:70px;top:168px;width:345px;font-size:19px;line-height:28px}

/* testimonials */
.testimonials{position:absolute;left:0;top:1800px;width:1200px;height:595px;background:linear-gradient(180deg,#fff 0%,#ececec 40%,#e4e4e4 70%,#fff 100%)}
.quote-box{position:absolute;left:222px;top:163px;width:750px;height:312px;background:var(--white);border:4px solid #dcdcdc;border-bottom:none}
.quote-box p{position:absolute;left:160px;top:60px;width:430px;text-align:center;font-size:17px;line-height:27px;color:var(--text)}
.qmark{position:absolute;font-family:Georgia,serif;font-size:56px;font-weight:700;color:var(--green);line-height:1}
.author{position:absolute;left:268px;top:235px;display:flex;align-items:center;gap:14px}
.avatar{width:50px;height:50px;border-radius:50%;border:2px solid #999}
.author b{display:block;font-size:14px;color:var(--ink)}
.author small{font-size:11px}
.arrow{position:absolute;top:2097px;width:44px;height:50px}

/* tips */
.tips{position:absolute;left:0;top:2395px;width:1200px;height:628px;background:var(--grey-bg)}
.post{position:absolute;top:178px;width:294px}
.post .ph{width:294px;height:222px}
.post h4{margin-top:28px;font-family:'Montserrat',sans-serif;font-weight:600;font-size:16px;color:var(--ink)}
.post p{margin-top:14px;font-size:12.5px;line-height:19px;width:270px}
.post .btn{position:relative;width:110px;height:33px;font-size:11px;margin-top:14px;margin-left:3px}

/* join */
.join{position:absolute;left:0;top:3023px;width:1200px;height:375px;background:linear-gradient(180deg,#16a6e3 0%,#1a86d6 60%,#2873cc 100%);color:var(--white);text-align:center}
.join h2{position:absolute;left:0;width:1200px;top:58px;font-family:'Montserrat',sans-serif;font-weight:600;font-size:40px}
.join p{position:absolute;left:0;width:1200px;top:112px;font-size:18px}
.field{position:absolute;top:175px;width:330px;height:50px;background:var(--white);color:#444;font-size:12px;text-align:left;padding:16px 20px}

/* partners */
.partners{position:absolute;left:0;top:3398px;width:1200px;height:279px;background:var(--white)}
.partners h3{position:absolute;left:0;width:1200px;top:56px;text-align:center;font-family:'Montserrat',sans-serif;font-weight:500;font-size:18px;line-height:29px;color:var(--ink)}
.badge{position:absolute;background:#c9ced6}

/* cta */
.cta{position:absolute;left:0;top:3677px;width:1200px;height:298px;background:linear-gradient(180deg,#3a3a3a,#4a4a4a 50%,#2e2e2e)}
.cta h2{position:absolute;left:0;width:1200px;top:84px;text-align:center;font-family:'Montserrat',sans-serif;font-weight:600;font-size:30px;color:var(--white)}

/* footer */
.footer{position:absolute;left:0;top:3975px;width:1200px;height:332px;background:var(--footer);color:#ddd;font-size:11px}
.footer h5{position:absolute;top:48px;font-family:'Montserrat',sans-serif;font-size:11px;font-weight:700;color:var(--white)}
.fcol{position:absolute;top:82px;line-height:18px}
.fcol .row{display:flex;gap:14px;margin-bottom:14px;align-items:flex-start}
.soc{display:flex;align-items:center;gap:12px;margin-bottom:14px}
.soc i{width:24px;height:24px;border-radius:50%;background:var(--blue-dark)}
.copy{position:absolute;left:0;width:1200px;top:286px;text-align:center;font-size:10px}
</style>
</head>
<body>

<header class="site-header">
  <div class="brand" style="left:130px;top:38px">
    <span class="brand-name" style="font-size:32px;color:#6d6d6d">Leadvista</span>
    <span class="brand-dot"></span>
  </div>
  <div class="follow">FOLLOW US <span class="s"></span><span class="s"></span><span class="s"></span><span class="s r"></span><span class="s g"></span></div>
  <div class="btn" style="left:878px;top:22px;width:190px;height:38px;font-size:15px">SUBSCRIBE NOW</div>
  <nav class="nav"><span class="on">HOME</span><span>ABOUT</span><span>SHOP</span><span>BOOKS</span><span>BLOG</span><span>EXECUTIVE HEALTH</span><span>CONTACT</span></nav>
</header>

<section class="hero" role="img" aria-label="Woman with open arms in a golden meadow at sunset">
  <div class="hero-text">
    <h1>Lead Vista</h1>
    <p>Take Yourself Up to the Next Level.</p>
    <ul>
      <li><svg width="16" height="14" viewBox="0 0 16 14"><path d="M2 7l4 4 8-9" fill="none" stroke="#fff" stroke-width="3"/></svg>More Success</li>
      <li><svg width="16" height="14" viewBox="0 0 16 14"><path d="M2 7l4 4 8-9" fill="none" stroke="#fff" stroke-width="3"/></svg>Higher Productivity</li>
      <li><svg width="16" height="14" viewBox="0 0 16 14"><path d="M2 7l4 4 8-9" fill="none" stroke="#fff" stroke-width="3"/></svg>Better Health</li>
    </ul>
  </div>
  <div class="dots"><i></i><i class="on"></i><i></i><i></i></div>
</section>

<section class="topics">
  <h2 class="sec-title" style="top:46px;font-size:29px;line-height:39px">This site provides you with<br>eye opening advice on</h2>

  <div class="card" style="left:30px;top:176px"><svg width="62" height="62" viewBox="0 0 62 62"><path d="M31 38C18 28 14 22 19 15c4-5 10-3 12 2 2-5 8-7 12-2 5 7 1 13-12 23z" fill="#16a6e3"/><path d="M4 44h14l10 6h20l10-6v8l-12 6H22L4 52z" fill="#16a6e3"/></svg>HEALTH &amp;<br>PRODUCTIVITY</div>
  <div class="card" style="left:264px;top:176px"><svg width="62" height="62" viewBox="0 0 62 62"><circle cx="31" cy="14" r="7" fill="#16a6e3"/><path d="M31 24l-8 34h16z" fill="#16a6e3"/><path d="M6 22l14 10M56 22L42 32M10 8l8 10M52 8l-8 10" stroke="#16a6e3" stroke-width="5" stroke-linecap="round"/></svg>STRESS REDUCTION<br>&amp; SLEEP</div>
  <div class="card active" style="left:497px;top:176px"><svg width="62" height="62" viewBox="0 0 62 62"><circle cx="26" cy="10" r="7" fill="#fff"/><path d="M20 22v18h18l8 14" fill="none" stroke="#fff" stroke-width="6" stroke-linecap="round"/><circle cx="22" cy="42" r="13" fill="none" stroke="#fff" stroke-width="5"/></svg>EXERCISE<span class="rm">READ MORE</span></div>
  <div class="card" style="left:728px;top:176px"><svg width="62" height="62" viewBox="0 0 62 62"><circle cx="28" cy="32" r="22" fill="none" stroke="#16a6e3" stroke-width="6"/><path d="M30 36l24-14 4 4-18 16 4 10-4 2-8-10z" fill="#16a6e3"/></svg>TRAVELING</div>
  <div class="card" style="left:961px;top:176px"><svg width="62" height="62" viewBox="0 0 62 62"><circle cx="31" cy="12" r="7" fill="#16a6e3"/><path d="M6 6l8 16h34l8-16-6-2-6 12H18L12 4zM22 22h18l-2 20 4 16H20l4-16z" fill="#16a6e3"/></svg>STRESS MANAGEMENT<br>COURSES</div>

  <div class="card" style="left:30px;top:395px"><svg width="62" height="62" viewBox="0 0 62 62"><circle cx="31" cy="14" r="7" fill="#16a6e3"/><path d="M10 22h42v8H38v28H24V30H10z" fill="#16a6e3"/></svg>FITNESS BOOT CAMPS<br>FOR EXECUTIVES</div>
  <div class="card" style="left:264px;top:395px"><svg width="62" height="62" viewBox="0 0 62 62"><circle cx="31" cy="10" r="7" fill="#16a6e3"/><path d="M22 20h18l6 16-6 2H22l-6-2z" fill="#16a6e3"/><path d="M6 50c10-8 40-8 50 0v6H6z" fill="#16a6e3"/></svg>MINDFULNESS<br>COURSES</div>
  <div class="card" style="left:497px;top:395px"><svg width="62" height="62" viewBox="0 0 62 62"><path d="M30 12a20 20 0 1 0 20 26 16 16 0 0 1-20-26z" fill="#16a6e3"/><path d="M44 6l2 5 5 1-4 3 1 5-4-3-4 3 1-5-4-3 5-1z" fill="#16a6e3"/><circle cx="52" cy="26" r="3" fill="#16a6e3"/></svg>COURSES FOR<br>HEALTHY SLEEP</div>
  <div class="card" style="left:728px;top:395px"><svg width="62" height="62" viewBox="0 0 62 62"><rect x="6" y="18" width="50" height="38" rx="3" fill="#16a6e3"/><rect x="22" y="8" width="18" height="10" fill="none" stroke="#16a6e3" stroke-width="4"/><path d="M20 18v38M42 18v38" stroke="#fff" stroke-width="3"/></svg>WORK-LIFE<br>BALANCE</div>
  <div class="card all" style="left:961px;top:395px"><svg width="26" height="24" viewBox="0 0 26 24"><path d="M3 3l9 9-9 9M13 3l9 9-9 9" fill="none" stroke="#fff" stroke-width="3"/></svg>VIEW ALL</div>
</section>

<div class="welcome-img" role="img" aria-label="Businessman walking up city stairs toward a skyline"></div>
<section class="welcome">
  <h3>Welcome to</h3>
  <h2>LEAD VISTA</h2>
  <p>To provide managers and executives with top in class health, fitness and diet advice so that they can reach the maximum productivity and energy level to be successful and happy in their business and private life.</p>
  <div class="btn" style="left:71px;top:368px;width:154px;height:43px;font-size:15px">READ MORE</div>
</section>

<section class="testimonials">
  <h2 class="sec-title" style="top:64px;font-size:38px">Testimonials</h2>
  <div class="quote-box">
    <span class="qmark" style="left:116px;top:38px">“</span>
    <p>In the past I thought that my success only depends on working harder and harder. Leadvista.com made me aware that I need to work smarter and that my success depends not only on my brain but also on my body.</p>
    <span class="qmark" style="left:496px;top:176px">”</span>
    <div class="author"><span class="avatar"></span><div><b>Marco Bellandi</b><small>VP Italy</small></div></div>
  </div>
</section>
<svg class="arrow" style="left:178px" viewBox="0 0 44 50"><path d="M44 0v50L0 25z" fill="#555"/><path d="M30 18l-7 7 7 7" fill="none" stroke="#fff" stroke-width="2"/></svg>
<svg class="arrow" style="left:970px" viewBox="0 0 44 50"><path d="M0 0v50l44-25z" fill="#555"/><path d="M14 18l7 7-7 7" fill="none" stroke="#fff" stroke-width="2"/></svg>

<section class="tips">
  <h2 class="sec-title" style="top:52px;font-size:28px;line-height:39px">Read the latest tips on<br>healthy productivity</h2>
  <article class="post" style="left:131px">
    <div class="ph" role="img" aria-label="Person sleeping in a blue-lit bedroom" style="background:linear-gradient(160deg,#2a5da8,#13305e)"></div>
    <h4>HEALTHY SLEEP</h4>
    <p>Do you toss (and turn) for hours at night and perhaps can't sleep until the wee hours of the morning?</p>
    <div class="btn">READ MORE</div>
  </article>
  <article class="post" style="left:452px">
    <div class="ph" role="img" aria-label="Woman relaxing on a sofa by the window" style="background:linear-gradient(160deg,#e8e2d4,#a89a84)"></div>
    <h4>GENERAL HEALTH</h4>
    <p>Are you suffering from eye fatigue, blurred vision or headaches? You may experience computer vision syndrome.</p>
    <div class="btn">READ MORE</div>
  </article>
  <article class="post" style="left:775px">
    <div class="ph" role="img" aria-label="Woman running against a concrete wall" style="background:linear-gradient(160deg,#c9c9c7,#8d8d8a)"></div>
    <h4>FITNESS</h4>
    <p>Tossing and turning all night, ruminating about tomorrow's big presentation? Running your mind over...</p>
    <div class="btn">READ MORE</div>
  </article>
</section>

<section class="join">
  <h2>Join the movement</h2>
  <p>Get free, exclusive tips in your inbox to become a healthy manager.</p>
  <div class="field" style="left:264px">NAME</div>
  <div class="field" style="left:605px">E MAIL</div>
  <div class="btn" style="left:532px;top:262px;width:136px;height:48px;font-size:16px">SIGNUP</div>
</section>

<section class="partners">
  <h3>THE WEBSITE CONTENT IS INSPIRED<br>BY THE RESEARCH AND PUBLICATIONS OF:</h3>
  <div class="badge" style="left:138px;top:166px;width:48px;height:60px;border-radius:6px"></div>
  <div class="badge" style="left:296px;top:178px;width:120px;height:32px"></div>
  <div class="badge" style="left:522px;top:180px;width:150px;height:30px"></div>
  <div class="badge" style="left:790px;top:164px;width:60px;height:60px;background:#2f78c4"></div>
  <div class="badge" style="left:951px;top:178px;width:38px;height:38px;border-radius:50%"></div>
</section>

<section class="cta" role="img" aria-label="Dark city backdrop behind a man walking">
  <h2>Start your path to health &amp; success now!</h2>
  <div class="btn" style="left:490px;top:153px;width:221px;height:50px;font-size:17px">SUBSCRIBE NOW</div>
</section>

<footer class="footer">
  <div class="brand" style="left:152px;top:112px">
    <span class="brand-name" style="font-size:30px;color:#fff">Leadvista</span>
    <span class="brand-dot"></span>
  </div>
  <h5 style="left:523px">CONTACT US</h5>
  <div class="fcol" style="left:523px">
    <div class="row"><svg width="10" height="14" viewBox="0 0 10 14"><path d="M5 0a5 5 0 0 1 5 5c0 4-5 9-5 9S0 9 0 5a5 5 0 0 1 5-5z" fill="#fff"/><circle cx="5" cy="5" r="2" fill="#222"/></svg><span>2150 Maple Ridge Road<br>Fairview, CA 90000</span></div>
    <div class="row"><svg width="12" height="12" viewBox="0 0 12 12"><path d="M2 0l3 3-2 2c1 2 2 3 4 4l2-2 3 3-2 2C5 12 0 7 0 2z" fill="#fff"/></svg><span>555.010.2040</span></div>
    <div class="row"><svg width="12" height="10" viewBox="0 0 12 10"><rect width="12" height="10" fill="#fff"/><path d="M0 0l6 5 6-5" fill="none" stroke="#222"/></svg><span>info@leadvista.com</span></div>
  </div>
  <h5 style="left:759px">MENU</h5>
  <div class="fcol" style="left:759px;line-height:17.5px">HOME<br>ABOUT<br>SHOP<br>BOOKS<br>BLOG<br>EXECUTIVE HEALTH<br>CONTACT</div>
  <h5 style="left:945px">CONNECT WITH US</h5>
  <div class="fcol" style="left:945px;top:78px">
    <div class="soc"><i></i>Community</div>
    <div class="soc"><i style="background:var(--blue)"></i>Updates</div>
    <div class="soc"><i style="background:#14396e"></i>Network</div>
  </div>
  <div class="copy">Copyrights @ 2019 All Rights Reserved</div>
</footer>

</body>
</html>
```